Vesprine Oakville Cabernet Sauvignon-Wine label design

We need a package design for an up market wine brand named, Vesprine. It will be a Cabernet Sauvignon from the Oakville AVA of Napa Valley. We are looking for a stylish modern label that will stand out on a retail shelf. We want the label to be attention grabbing and stylish while presenting an up market luxury brand.

Sick

Requirements
Must have
• Must have the words(in order of importance)
-Vesprine
-Cabernet Sauvignon
-Oakville
-Napa Valley
-2018

Must be designed for a traditional "Bordeaux" style bottle (Bottle specs in uploaded files)
Should not have
• Any images of grapes, vineyards, wine glasses or bottles

```html
<!DOCTYPE html>
<html lang="en">
<head>
<meta charset="utf-8">
<title>Vesprine Cabernet Sauvignon – Wine Label</title>
<link rel="stylesheet" href="https://fonts.googleapis.com/css2?family=Stint+Ultra+Condensed&family=Libre+Caslon+Text&display=swap">
<style>
  :root {
    --backdrop: #d9d6dc;
    --label-cream: #fcebd6;
    --wine-red: #b51f2a;
    --ink: #3a3a42;
    --teal: #3fb3c2;
    --orange: #e0832a;
    --sand: #f4c98a;
    --cocoa: #5a1e14;
    --frame-stripes: var(--wine-red) 0 10px, var(--sand) 10px 16px,
      var(--teal) 16px 24px, var(--orange) 24px 32px, var(--cocoa) 32px 38px;
  }
  * { margin: 0; padding: 0; box-sizing: border-box; }
  html, body {
    width: 1200px;
    height: 888px;
    overflow: hidden;
    background: var(--backdrop);
  }
  .canvas {
    position: relative;
    width: 1200px;
    height: 888px;
  }
  .label {
    position: absolute;
    left: 288px;
    top: 64px;
    width: 624px;
    height: 760px;
    background: var(--label-cream);
  }
  .frame-edge {
    position: absolute;
  }
  .frame-edge--top, .frame-edge--bottom {
    left: 0;
    width: 100%;
    height: 7px;
    background: repeating-linear-gradient(90deg, var(--frame-stripes));
  }
  .frame-edge--top { top: 0; }
  .frame-edge--bottom { bottom: 0; }
  .frame-edge--left, .frame-edge--right {
    top: 0;
    width: 7px;
    height: 100%;
    background: repeating-linear-gradient(180deg, var(--frame-stripes));
  }
  .frame-edge--left { left: 0; }
  .frame-edge--right { right: 0; }
  .floral-panel {
    position: absolute;
    left: 153px;
    top: 49px;
    width: 317px;
    height: 323px;
    background:
      radial-gradient(circle at 20% 35%, var(--teal) 0 14%, transparent 26%),
      radial-gradient(circle at 18% 82%, var(--wine-red) 0 10%, transparent 20%),
      radial-gradient(circle at 60% 45%, var(--sand) 0 18%, transparent 38%),
      linear-gradient(135deg, var(--orange), var(--cocoa) 55%, var(--teal));
  }
  .varietal {
    position: absolute;
    top: 410px;
    width: 100%;
    text-align: center;
    font-family: "Libre Caslon Text", serif;
    font-size: 24px;
    line-height: 32px;
    color: var(--wine-red);
  }
  .brand-name {
    position: absolute;
    top: 450px;
    width: 100%;
    height: 190px;
    text-align: center;
    font-family: "Stint Ultra Condensed", serif;
    font-weight: 400;
    font-size: 210px;
    line-height: 190px;
    letter-spacing: 3px;
    color: var(--ink);
  }
  .origin {
    position: absolute;
    top: 644px;
    width: 100%;
    display: flex;
    justify-content: center;
    gap: 18px;
    font-family: "Libre Caslon Text", serif;
    font-size: 18px;
    line-height: 24px;
    color: var(--wine-red);
  }
  .vintage {
    position: absolute;
    top: 683px;
    width: 100%;
    text-align: center;
    font-family: "Libre Caslon Text", serif;
    font-size: 24px;
    line-height: 30px;
    color: var(--ink);
  }
</style>
</head>
<body>
  <main class="canvas">
    <section class="label">
      <div class="frame-edge frame-edge--top" role="img" aria-label="Border of small multicoloured dashes in red, teal, orange and brown"></div>
      <div class="frame-edge frame-edge--right"></div>
      <div class="frame-edge frame-edge--bottom"></div>
      <div class="frame-edge frame-edge--left"></div>
      <div class="floral-panel" role="img" aria-label="Square illustration of stylised flowers and leaves in orange, teal, cream, brown and red"></div>
      <p class="varietal">Cabernet Sauvignon</p>
      <h1 class="brand-name">VESPRINE</h1>
      <p class="origin"><span>Oakville</span><span>Napa valley</span></p>
      <p class="vintage">2018</p>
    </section>
  </main>
</body>
</html>
```